Beef cattle farm needs signs which can be seen from roadside

We would like submissions of artwork for a sign that will hang from a fence or gate and will be seen by passing cars.

Existing logo and branding theme for the company is attached.

Signage can be between 900mm x 400mm - 1200mm x 600mm

Industry/Entity Type

Farm

Requirements
Must have
• the Signs should have the following information:
• Company name: Brindle Ridge Grazing Company
• Address: 214 Wattlebank Hollow Road
• Contact number: 0431 862 475
• email address: admin@brindleridgegrazingco.com.au
• - Logo and branding as per attached artwork

```html
<!DOCTYPE html>
<html lang="en">
<head>
<meta charset="utf-8">
<title>Brindle Ridge Grazing Company – Roadside Sign</title>
<link rel="stylesheet" href="https://fonts.googleapis.com/css2?family=Montserrat:wght@500&family=Arimo:wght@400;700&display=swap">
<style>
  :root {
    --backdrop: #b9b6b6;
    --sign-white: #ffffff;
    --farm-green: #116233;
    --divider-grey: #9a9898;
    --text-light: #ffffff;
  }
  html, body {
    margin: 0;
    padding: 0;
    width: 1200px;
    height: 655px;
    overflow: hidden;
    background: var(--backdrop);
  }
  .sign {
    position: absolute;
    left: 109px;
    top: 109px;
    width: 982px;
    height: 436px;
    background: var(--sign-white);
  }
  .brand {
    position: absolute;
    left: 72px;
    top: 30px;
    width: 860px;
    height: 258px;
    display: flex;
    align-items: center;
    gap: 48px;
  }
  .brand-dot {
    flex: none;
    width: 256px;
    height: 256px;
  }
  .brand-name {
    margin: 0;
    font-family: "Montserrat", sans-serif;
    font-weight: 500;
    color: var(--farm-green);
    line-height: 1.1;
    text-transform: uppercase;
  }
  .brand-name .line-main {
    display: block;
    font-size: 60px;
    letter-spacing: 1px;
  }
  .brand-name .line-sub {
    display: block;
    font-size: 40px;
    letter-spacing: 1px;
    margin-top: 10px;
  }
  .divider {
    position: absolute;
    left: 0;
    top: 308px;
    width: 100%;
    height: 8px;
    background: var(--divider-grey);
  }
  .contact-band {
    position: absolute;
    left: 0;
    top: 316px;
    width: 100%;
    height: 120px;
    background: var(--farm-green);
    color: var(--text-light);
    font-family: "Arimo", sans-serif;
  }
  .phone {
    position: absolute;
    left: 61px;
    top: 24px;
    margin: 0;
    font-size: 35px;
    font-weight: 700;
  }
  .email {
    position: absolute;
    left: 60px;
    top: 73px;
    margin: 0;
    font-size: 20px;
    font-weight: 700;
  }
  .address {
    position: absolute;
    right: 33px;
    top: 62px;
    margin: 0;
    font-size: 23px;
    font-weight: 400;
  }
</style>
</head>
<body>
  <main class="sign">
    <header class="brand">
      <svg class="brand-dot" viewBox="0 0 256 256" aria-hidden="true">
        <circle cx="128" cy="128" r="128" fill="var(--farm-green)"/>
      </svg>
      <h1 class="brand-name">
        <span class="line-main">Brindle Ridge</span>
        <span class="line-sub">Grazing Company</span>
      </h1>
    </header>
    <div class="divider"></div>
    <footer class="contact-band">
      <p class="phone">Call : 0431 862 475</p>
      <p class="email">admin@brindleridgegrazingco.com.au</p>
      <p class="address">214 Wattlebank Hollow Road</p>
    </footer>
  </main>
</body>
</html>
```